PLV Flyer

We need a professional design for flyers that we produce. The attached event draft is typical of the majority of flyers we will produce, and is the one that we need to do right now.

We would also like the source files for the design. We don’t have Corel Draw, but can work with any files produced in Adobe Creative Suite products.

Target Market(s)

Owners of residential apartments

Industry/Entity Type

Non-Profit

Requirements
Must have
• Design must be complimentary to our new website design at www.plv.org.au so we can establish consistent branding.
• Any fonts used must be freely avalaible standard fonts used in Microsoft Word

```html
<!DOCTYPE html>
<html lang="en">
<head>
<meta charset="utf-8">
<title>PLV Educational Workshop Flyer</title>
<link rel="stylesheet" href="https://fonts.googleapis.com/css2?family=Arimo:ital,wght@0,400;0,700;1,700&family=Roboto+Condensed:wght@700&display=swap">
<style>
:root{
  --navy:#1f3a86;
  --blue:#2563ad;
  --gold:#e3a732;
  --gold-dark:#cf9632;
  --ink:#1b1b1b;
  --panel:#dcdde0;
  --rule:#8a8d95;
  --white:#ffffff;
}
*{margin:0;padding:0;box-sizing:border-box}
html,body{width:849px;height:1200px;overflow:hidden;background:var(--white)}
.flyer{position:relative;width:849px;height:1200px;font-family:"Arimo",Arial,sans-serif;color:var(--ink);overflow:hidden}
.abs{position:absolute}

.brand{left:42px;top:62px;display:flex;align-items:flex-start;gap:22px}
.brand-mark{width:54px;height:54px;background:var(--gold);margin-top:44px}
.brand-name{font-family:"Arimo",Arial,sans-serif;font-weight:400;color:var(--navy);font-size:35px;line-height:32px;letter-spacing:3px;text-transform:uppercase;padding-top:22px}

.photo{background:linear-gradient(135deg,#e9ecef 0%,#c9cfd6 45%,#7a8391 100%)}
.photo-header{left:538px;top:0;width:311px;height:203px;border:1px solid #9aa0a8}
.photo-team{left:0;top:297px;width:331px;height:470px;background:linear-gradient(160deg,#eef0f2 0%,#b9c3cf 40%,#7d95b8 70%,#e7e9ec 100%)}

.title-band{left:0;top:205px;width:849px;height:55px;background:linear-gradient(180deg,var(--gold) 0%,var(--gold) 55%,var(--gold-dark) 56%,var(--gold-dark) 100%);display:flex;align-items:center;justify-content:center}
.title-band h1{font-weight:700;font-size:23px;color:var(--white);letter-spacing:.6px}
.subtitle-band{left:0;top:263px;width:849px;height:30px;background:var(--navy);display:flex;align-items:center;justify-content:center}
.subtitle-band p{font-style:italic;font-weight:700;font-size:13.4px;color:var(--white);letter-spacing:1.45px}
.gold-rule{left:0;top:294px;width:849px;height:3px;background:var(--gold)}

.register-bar{left:0;top:771px;width:331px;height:39px;background:var(--blue);display:flex;align-items:center;justify-content:center;font-family:"Roboto Condensed",sans-serif;font-weight:700;color:var(--white);font-size:18.5px;letter-spacing:.4px}

.cond{font-family:"Roboto Condensed",sans-serif;font-weight:700;color:var(--navy)}
.details{left:349px;top:0;width:480px;font-size:12px}
.details .row{position:absolute;left:0;white-space:nowrap;line-height:16px}
.details .head{font-size:17px;left:5px}
.details .lbl{font-size:16px}
.details .and{font-size:13px;left:15px}
.bullet{left:5px}

.schedule-panel{left:331px;top:810px;width:518px;height:222px;background:var(--panel);border-top:1px solid var(--rule);border-left:1px solid var(--rule);border-bottom:1px solid var(--rule)}
.schedule-panel h2{position:absolute;left:11px;top:16px;font-size:16.5px}
.schedule{position:absolute;left:9px;top:47px;width:495px;height:161px;border:1px solid #6e7078;border-radius:14px;overflow:hidden;background:var(--white)}
.schedule table{width:100%;height:100%;border-collapse:collapse;font-size:12px}
.schedule th{background:var(--blue);color:var(--white);font-weight:700;height:27px;font-size:12px}
.schedule td{border-top:1px solid #6e7078;border-left:1px solid #6e7078;padding:0 9px;line-height:21px;vertical-align:middle}
.schedule td:first-child,.schedule th:first-child{border-left:none}
.schedule th+th{border-left:1px solid #6e7078}
.col-time{width:80px}.col-topic{width:145px}

.theme{left:26px;top:826px;font-size:12px}
.theme h2{font-size:16.5px;margin-bottom:6px}
.theme-text{line-height:25.6px}
.theme-wrap{left:23px;top:1058px;width:810px;font-size:12px;line-height:25.6px}

.footer-band{left:0;top:1153px;width:849px;height:47px;background:linear-gradient(180deg,var(--gold) 0%,var(--gold-dark) 100%);display:flex;align-items:center;justify-content:center;font-family:"Roboto Condensed",sans-serif;font-weight:700;color:var(--white);font-size:15.7px;letter-spacing:.1px}
</style>
</head>
<body>
<div class="flyer">

  <header>
    <div class="abs brand">
      <div class="brand-mark"></div>
      <div class="brand-name">Precinct<br>Living<br>Voice</div>
    </div>
    <div class="abs photo photo-header" role="img" aria-label="Photo of a smiling businesswoman with colleagues at a meeting table"></div>
  </header>

  <div class="abs title-band"><h1>PLV Educational Workshop</h1></div>
  <div class="abs subtitle-band"><p>“The Essentials of Strata Living – What Every Owner Needs to Know” 12th and 26th June 2010</p></div>
  <div class="abs gold-rule"></div>

  <div class="abs photo photo-team" role="img" aria-label="Photo of three young professionals smiling while reviewing work at a desk"></div>
  <div class="abs register-bar">Register at www.plv.org.au</div>

  <section class="abs details">
    <div class="row head cond" style="top:321px">This Workshop Is For Owners In Strata Apartments Who Want</div>
    <div class="row head cond" style="top:347px">To Learn More About:</div>
    <div class="row bullet" style="top:374px">• getting the best out of apartment living</div>
    <div class="row bullet" style="top:400px">• protecting their home and their investment</div>
    <div class="row and cond" style="top:427px">AND particularly for...</div>
    <div class="row bullet" style="top:454px">• executive committee members to know their rights</div>
    <div class="row" style="top:479px;left:15px">and responsibilities in managing their strata scheme</div>
    <div class="row" style="top:516px"><span class="lbl cond">Location:</span> Harbourside Club 24 Wharf Parade Milsons Bay 2061</div>
    <div class="row" style="top:545px"><span class="lbl cond">Dates:</span> The workshop will run twice – on 12th June and 26th June 2010</div>
    <div class="row" style="top:573px"><span class="lbl cond">Time:</span> 10.00 am to 4.00 pm.</div>
    <div class="row" style="top:602px"><span class="lbl cond">Cost:</span> $60.00, which includes morning tea and lunch.</div>
    <div class="row" style="top:631px">The maximum number of participants for each workshop is 60.</div>
    <div class="row lbl cond" style="top:661px">Register at www.plv.org.au</div>
    <div class="row" style="top:688px"><span class="lbl cond">Programme:</span> The day will comprise four sessions, each facilitated by a specialist.</div>
    <div class="row" style="top:714px">In each session the speaker will provide relevant information and set the topics for</div>
    <div class="row" style="top:740px">group work; participants will break into groups and work up solutions to each topic;</div>
    <div class="row" style="top:766px">and the groups will compare outcomes.</div>
  </section>

  <section class="abs theme">
    <h2 class="cond">The Day’s Theme Will Be:</h2>
    <p class="theme-text">Gina is a new owner in her building called Utopia<br>Tower. She notices some management processes<br>which to her seem strange. She is elected to the<br>executive committee and finds that the developer has<br>retained more control than she realised - the service<br>providers have long-term and onerous contracts,<br>and she doesn’t seem to be able to exert enough<br>influence. What does the law require her to do, as a</p>
  </section>
  <p class="abs theme-wrap">committee member? How does she influence good management processes? The finances seem to be out of control, so how can she fix them so she doesn’t pay inflated levies each year and lose value on her investment? ... and then the neighbour above her apartment installs a timber floor and she has noise problems ... and the building seems to have a lot of defects ............</p>

  <section class="abs schedule-panel">
    <h2 class="cond">Conference Schedule:</h2>
    <div class="schedule">
      <table>
        <thead><tr><th class="col-time"></th><th class="col-topic">Topic</th><th>Speaker</th></tr></thead>
        <tbody>
          <tr style="height:27px"><td rowspan="2">Morning</td><td>Governance</td><td>Martin Hale, strata lawyer</td></tr>
          <tr style="height:52px"><td>Management</td><td>Stephen Dorr, seasoned former chairperson and executive committee member</td></tr>
          <tr style="height:24px"><td rowspan="2">Afternoon</td><td>Financials</td><td>Peter Lawson, accountant</td></tr>
          <tr style="height:30px"><td>Physicality</td><td>Daniel Ferris, facilities manager</td></tr>
        </tbody>
      </table>
    </div>
  </section>

  <footer class="abs footer-band">Enroll Now - Learn A Lot - Have Some Fun As Well - Share Experiences - Find Out How PLV Can Help You In The Longer Term</footer>

</div>
</body>
</html>
```